Business card for denture clinic Gumlyssa

We need a new business card with our new logo. We are a denture clinic in New Zealand with our target market being 45+ years old. We would need a space on the back to write our patients next appointment on. We would space for only one appointment rather than a list. We will attach a photo showing an example of this. But of course, we would like to see your twist on this. We want it to be bold and easy to read and a good mixture of professional but modern. We have attached our logo to be used on the card.

Target Market(s)

People aged 45+ needing dentures

Industry/Entity Type

Dental

Contact Information for Business Card

We want our logo on the front and the space to write an appointment on the back. I've attached an example our our old business card showing this. We need to have the technicians details on the front.

Font styles to use
Sans Serif

Colors
0255a3
919191
fbfbfb

Requirements
Must have
• The following details:
• Ravi Pelling BDT, PGDipCDentTech Marlow
• Dental Prosthetist
• Phone numbers: 0800 47 2150
• 09 571 3294
• Email: ravi@gumlyssa.co.nz
• www.gumlyssa.co.nz
• Address: 418 Whiroa Road
• Kauriwhenua East
• Auckland 0610
Nice to have
• We would like our business cards to have more than just two colours as we want them to be more vibrant. We have uploaded an example of a business card we liked that showed this.

```html
<!DOCTYPE html>
<html lang="en">
<head>
<meta charset="utf-8">
<title>Gumlyssa – Business Card</title>
<link href="https://fonts.googleapis.com/css2?family=Open+Sans:wght@300;400;600&family=Oswald:wght@500&display=swap" rel="stylesheet">
<style>
  :root {
    --brand-blue: #0255a3;
    --accent-blue: #2f86d4;
    --grey: #919191;
    --paper: #fbfbfb;
    --card-dark: #141414;
    --card-mid: #2c2c2c;
    --backdrop: #d8d3cd;
  }
  * { box-sizing: border-box; margin: 0; padding: 0; }
  html, body {
    width: 1200px; height: 1000px; overflow: hidden;
    background: var(--backdrop);
    font-family: "Open Sans", Arial, sans-serif;
  }
  .sheet {
    width: 1200px; height: 1000px;
    display: flex; flex-direction: column; align-items: center; justify-content: center;
    gap: 40px;
  }
  .card {
    position: relative;
    width: 720px; height: 440px;
    border-radius: 6px;
    background: linear-gradient(135deg, var(--card-mid) 0%, var(--card-dark) 55%, #0c0c0c 100%);
    box-shadow: 0 10px 24px rgba(0,0,0,.28);
    color: var(--paper);
    overflow: hidden;
  }

  /* Appointment side */
  .brand {
    position: absolute; top: 80px; left: 0; right: 0;
    display: flex; flex-direction: column; align-items: center;
  }
  .brand-row { display: flex; align-items: center; gap: 14px; }
  .brand-square { width: 46px; height: 46px; background: var(--accent-blue); border-radius: 4px; }
  .brand-name {
    font-weight: 600; font-size: 40px; letter-spacing: 2px;
    color: var(--accent-blue); text-transform: uppercase;
  }
  .brand-tagline {
    margin-top: 4px; font-size: 13px; letter-spacing: 3.4px;
    color: var(--grey); text-transform: uppercase; padding-left: 60px;
  }
  .appointment { position: absolute; left: 56px; right: 56px; top: 262px; }
  .appointment-title {
    font-size: 17px; font-weight: 600; letter-spacing: 1.5px;
    color: var(--accent-blue); text-transform: uppercase; margin-bottom: 28px;
  }
  .appointment-row {
    display: flex; align-items: baseline; gap: 8px;
    font-size: 18px; font-weight: 300; color: var(--paper);
  }
  .appointment-row .fill {
    flex: 1; border-bottom: 2px dotted var(--grey); height: 1px; margin-right: 10px;
  }
  .appointment-row .fill:last-child { margin-right: 0; }

  /* Contact side */
  .identity {
    position: absolute; left: 40px; top: 150px; width: 330px; text-align: right;
  }
  .person-name {
    font-family: "Oswald", "Arial Narrow", sans-serif;
    font-weight: 500; font-size: 38px; letter-spacing: 1.5px;
    text-transform: uppercase; color: var(--paper); line-height: 1.1;
  }
  .person-credential {
    font-size: 14px; font-weight: 400; color: var(--grey);
    letter-spacing: .5px; margin-top: 4px;
  }
  .person-role { font-size: 19px; color: var(--accent-blue); margin-top: 2px; }
  .divider {
    position: absolute; left: 392px; top: 146px; width: 2px; height: 126px;
    background: var(--grey);
  }
  .contacts { position: absolute; left: 414px; top: 151px; list-style: none; }
  .contacts li {
    display: flex; align-items: center; gap: 12px;
    font-size: 16px; font-weight: 300; line-height: 29px; color: var(--paper);
  }
  .contacts svg { width: 14px; height: 14px; flex: none; }
  .contacts .highlight { color: var(--accent-blue); }
  .address {
    position: absolute; left: 70px; bottom: 46px;
    display: flex; align-items: center; gap: 12px;
    font-size: 18px; font-weight: 300; color: var(--paper);
  }
  .address svg { width: 16px; height: 18px; }
</style>
</head>
<body>
<main class="sheet">

  <section class="card card--appointment" aria-label="Card back: appointment">
    <div class="brand">
      <div class="brand-row">
        <span class="brand-square"></span>
        <span class="brand-name">Gumlyssa</span>
      </div>
      <div class="brand-tagline">The Denture Experts</div>
    </div>
    <div class="appointment">
      <h2 class="appointment-title">Your Next Appointment</h2>
      <div class="appointment-row">date:<span class="fill"></span>time:<span class="fill"></span>day:<span class="fill"></span></div>
    </div>
  </section>

  <section class="card card--contact" aria-label="Card front: technician details">
    <div class="identity">
      <h1 class="person-name">Ravi Pelling BDT</h1>
      <p class="person-credential">PGDipCDentTech Marlow</p>
      <p class="person-role">Dental Prosthetist</p>
    </div>
    <div class="divider"></div>
    <ul class="contacts">
      <li>
        <svg viewBox="0 0 14 14" aria-hidden="true"><path d="M3 1l2.5 3-1.5 1.6c.8 1.8 2.2 3.2 4 4L9.6 8 13 10.5 11.5 13C6 12.5 1.5 8 1 2.5z" fill="var(--accent-blue)"/></svg>
        0800 47 2150
      </li>
      <li>
        <svg viewBox="0 0 14 14" aria-hidden="true"><rect x="3.5" y="1" width="7" height="12" rx="1.2" fill="none" stroke="var(--accent-blue)" stroke-width="1.5"/><circle cx="7" cy="11" r=".8" fill="var(--accent-blue)"/></svg>
        09 571 3294
      </li>
      <li>
        <svg viewBox="0 0 14 14" aria-hidden="true"><rect x="1" y="3" width="12" height="8.5" rx="1" fill="var(--accent-blue)"/><path d="M1.5 3.5L7 8l5.5-4.5" fill="none" stroke="var(--card-dark)" stroke-width="1.2"/></svg>
        ravi@gumlyssa.co.nz
      </li>
      <li>
        <svg viewBox="0 0 14 14" aria-hidden="true"><circle cx="7" cy="7" r="5.5" fill="none" stroke="var(--accent-blue)" stroke-width="1.4"/><path d="M1.5 7h11M7 1.5c-2.4 3-2.4 8 0 11M7 1.5c2.4 3 2.4 8 0 11" fill="none" stroke="var(--accent-blue)" stroke-width="1"/></svg>
        <span>www.<span class="highlight">gumlyssa</span>.co.nz</span>
      </li>
    </ul>
    <p class="address">
      <svg viewBox="0 0 16 18" aria-hidden="true"><path d="M8 1a5.5 5.5 0 0 0-5.5 5.5C2.5 11 8 17 8 17s5.5-6 5.5-10.5A5.5 5.5 0 0 0 8 1z" fill="var(--accent-blue)"/><circle cx="8" cy="6.5" r="2" fill="var(--card-dark)"/></svg>
      418 Whiroa Road, Kauriwhenua East, Auckland 0610
    </p>
  </section>

</main>
</body>
</html>
```